Mine Engineering Consultancy specializing in
* Pit optimization
* Mine Design
* Scheduling
* Mine Rehabilitation

Industry/Entity Type

Mining

Contact Information for Business Card

RVT Mining Pty Ltd
Derek Holloway
Director/Principle Mining Engineer
Mobile 0413582961
Email derek.holloway@rvtmining-example.com

```html
<!DOCTYPE html>
<html lang="en">
<head>
<meta charset="utf-8">
<title>RVT Mining Pty Ltd – Business Card</title>
<link rel="stylesheet" href="https://fonts.googleapis.com/css2?family=Open+Sans:ital,wght@0,400;0,600;0,700;1,400&display=swap">
<style>
  :root {
    --backdrop: #3b3b3b;
    --card-white: #f6f6f6;
    --brand-blue: #1565b8;
    --text-dark: #3a3a3a;
    --tab-dark: #3c3c3c;
    --rock-light: #8a8a88;
    --rock-mid: #5d5d5b;
    --rock-dark: #3f3f3e;
    --white: #ffffff;
  }
  * { margin: 0; padding: 0; box-sizing: border-box; }
  html, body {
    width: 1200px; height: 750px; overflow: hidden;
    background: var(--backdrop);
    font-family: "Open Sans", Arial, sans-serif;
  }
  .canvas { position: relative; width: 1200px; height: 750px; }

  .card {
    position: absolute; top: 228px;
    width: 461px; height: 263px;
    overflow: hidden;
  }
  .card--front { left: 124px; background: var(--card-white); }
  .card--back { left: 618px; }

  /* Front */
  .brand-name {
    position: absolute; left: 26px; top: 62px;
    font-size: 26px; font-weight: 400;
    color: var(--brand-blue); letter-spacing: 0.2px;
  }
  .edge-tab {
    position: absolute; top: 178px; width: 8px; height: 58px;
    border-radius: 4px;
  }
  .edge-tab--left { left: -2px; background: var(--brand-blue); }
  .edge-tab--right { right: -2px; background: var(--tab-dark); }

  .contact-list {
    position: absolute; left: 26px; top: 180px;
    list-style: none;
    font-size: 10px; color: var(--text-dark);
  }
  .contact-item {
    display: flex; align-items: center; gap: 6px;
    height: 17.5px;
  }
  .contact-icon { width: 11px; height: 11px; flex: none; }

  .person {
    position: absolute; right: 21px; top: 186px;
    text-align: right;
  }
  .person-name {
    font-size: 16.5px; font-weight: 600; color: var(--brand-blue);
    line-height: 1.2;
  }
  .person-title {
    font-size: 11.5px; color: var(--text-dark); line-height: 1.4;
  }

  /* Back */
  .site-photo {
    position: absolute; inset: 0;
    background: linear-gradient(160deg, var(--rock-light) 0%, var(--rock-mid) 45%, var(--rock-dark) 75%, var(--rock-mid) 100%);
  }
  .back-brand {
    position: absolute; left: 0; right: 0; top: 88px;
    text-align: center;
    font-size: 26px; font-weight: 400; color: var(--brand-blue);
  }
  .services-band {
    position: absolute; left: 0; right: 0; top: 192px; height: 42px;
    background: var(--brand-blue); color: var(--white);
    text-align: center; padding-top: 4px;
  }
  .services-heading { font-size: 11.5px; font-weight: 600; line-height: 1.4; }
  .services-list { font-size: 10.5px; font-style: italic; line-height: 1.6; }
</style>
</head>
<body>
<main class="canvas">

  <section class="card card--front" aria-label="Business card front">
    <div class="brand-name">RVT Mining Pty Ltd</div>
    <span class="edge-tab edge-tab--left"></span>
    <span class="edge-tab edge-tab--right"></span>

    <ul class="contact-list">
      <li class="contact-item">
        <svg class="contact-icon" viewBox="0 0 12 12" aria-hidden="true">
          <path d="M2.5 1 L4.3 1 L5 3.4 L3.8 4.4 Q5 7 7.6 8.2 L8.6 7 L11 7.7 L11 9.5 Q10.5 11 9 11 Q1 10 1 3 Q1 1.5 2.5 1 Z" fill="var(--brand-blue)"/>
        </svg>
        <span>0413582961</span>
      </li>
      <li class="contact-item">
        <svg class="contact-icon" viewBox="0 0 12 12" aria-hidden="true">
          <rect x="0.5" y="2.5" width="11" height="7.5" fill="var(--brand-blue)"/>
          <path d="M0.8 2.8 L6 6.8 L11.2 2.8" fill="none" stroke="var(--white)" stroke-width="1"/>
        </svg>
        <span>derek.holloway@rvtmining-example.com</span>
      </li>
      <li class="contact-item">
        <svg class="contact-icon" viewBox="0 0 12 12" aria-hidden="true">
          <circle cx="6" cy="6" r="5.5" fill="var(--brand-blue)"/>
          <path d="M6 0.5 V11.5 M0.5 6 H11.5 M2 3 H10 M2 9 H10" stroke="var(--white)" stroke-width="0.7" fill="none"/>
          <ellipse cx="6" cy="6" rx="2.4" ry="5.5" fill="none" stroke="var(--white)" stroke-width="0.7"/>
        </svg>
        <span>www.rvtmining-example.com</span>
      </li>
    </ul>

    <div class="person">
      <p class="person-name">Derek Holloway</p>
      <p class="person-title">Director/Principle Mining Engineer</p>
    </div>
  </section>

  <section class="card card--back" aria-label="Business card back">
    <div class="site-photo" role="img" aria-label="Photograph of an open-cut mine pit with terraced grey walls and a haul truck on the ramp"></div>
    <div class="back-brand">RVT Mining Pty Ltd</div>
    <div class="services-band">
      <p class="services-heading">Mine Engineering Consultancy specializing in</p>
      <p class="services-list">Pit optimization &nbsp;/&nbsp; Mine Design &nbsp;/&nbsp; Scheduling &nbsp;/&nbsp; Mine Rehabilitation</p>
    </div>
  </section>

</main>
</body>
</html>
```